Private lender of mortgages and rent to own housing

need a website that reflects real estate especially mortgage lending and rent to own houses..
Sections as follows
Home About Types of mortgages Rent to own Contact us
Target Market(s)
consumers who require non traditonal mortgages
Industry/Entity Type
Mortgage
Coding
Coded - Design and coding required
Number of Pages Required
4 page
Font styles to use
Sans Serif
Colors
Designer to choose colors to be used in the design.
Requirements
Must have
- background pictures on pages. with nice picture on homepage of houses or a community
Nice to have
- contact us form i supplied a ink to

```html
<!DOCTYPE html>
<html lang="en">
<head>
<meta charset="utf-8">
<title>Harbourline Lending Group</title>
<link rel="stylesheet" href="https://fonts.googleapis.com/css2?family=Jost:wght@400;500;600;700&display=swap">
<style>
:root{
  --navy:#25215f;
  --navy-dark:#1d1a50;
  --ink:#222;
  --text:#444;
  --muted:#999;
  --line:#cfcfd6;
  --panel:#f3f3f3;
  --white:#fff;
  --grey-icon:#9d9d9d;
  --footer-bar:#8b8b8b;
}
*{box-sizing:border-box;margin:0;padding:0}
html,body{width:1200px;height:2651px;overflow:hidden}
body{font-family:"Jost",sans-serif;color:var(--text);background:var(--white);position:relative}

/* header */
.topline{position:absolute;top:0;left:0;width:1200px;height:4px;background:var(--navy)}
.site-header{position:absolute;top:4px;left:0;width:1200px;height:84px;background:var(--white)}
.brand{position:absolute;left:141px;top:26px;display:flex;align-items:center;gap:10px;font-weight:700;font-size:15px;letter-spacing:.5px;color:var(--navy);white-space:nowrap}
.brand-mark{width:18px;height:18px;background:var(--navy)}
.header-contact{position:absolute;top:22px;display:flex;gap:10px;font-size:13px;color:var(--ink);line-height:17px;white-space:nowrap}
.header-contact svg{flex:none}
.hc-address{left:748px}
.hc-phone{left:932px}
.hc-phone b{font-weight:600}

/* hero */
.hero{position:absolute;top:88px;left:0;width:1200px;height:407px;background:linear-gradient(180deg,#cfc4b4 0%,#b3a693 35%,#6d5f54 60%,#4c4f3f 80%,#2f3527 100%)}
.nav{position:absolute;top:4px;left:141px;width:778px;height:46px;background:rgba(210,210,214,.82)}
.nav a{position:absolute;top:6px;font-size:12px;font-weight:600;letter-spacing:.6px;color:var(--white);text-decoration:none;text-transform:uppercase;height:34px;line-height:34px;white-space:nowrap;text-shadow:0 1px 1px rgba(0,0,0,.2)}
.nav a.active{left:7px;width:114px;text-align:center;background:var(--navy)}
.nav .n-about{left:156px}
.nav .n-types{left:290px}
.nav .n-rent{left:504px}
.nav .n-contact{left:663px}
.nav-social{position:absolute;top:4px;left:919px;width:140px;height:46px;background:var(--navy);display:flex;align-items:center;justify-content:center;gap:22px;clip-path:polygon(6% 0,100% 0,100% 100%,0 100%)}
.nav-social span{width:10px;height:10px;border-radius:50%;background:var(--white)}
.hero-caption{position:absolute;left:141px;top:330px;width:740px;font-size:24px;line-height:30px;color:var(--white);letter-spacing:.5px}
.hero-caption b{font-weight:600}
.hero-dots{position:absolute;left:1014px;top:361px;display:flex;gap:10px}
.hero-dots i{width:7px;height:7px;background:#bbb}
.hero-dots i.on{background:var(--white)}

/* headings */
.divider{height:2px;background:var(--line);position:relative}
.divider::after{content:"";position:absolute;left:50%;top:-4px;width:8px;height:8px;margin-left:-4px;background:var(--white);border:1px solid var(--line)}
.section-title{font-size:30px;font-weight:400;color:var(--navy);text-align:center;letter-spacing:.5px;white-space:nowrap}
.section-title b{font-weight:600}
.title-block{position:absolute;left:0;width:1200px}
.title-block .divider{margin:14px auto 0;width:440px}

/* about */
.about{position:absolute;top:495px;left:0;width:1200px;height:397px}
.about-text{left:141px;width:616px;top:47px;position:absolute}
.about-text .section-title{text-align:left}
.about-text .divider{margin:10px 0 14px}
.about-text .divider::after{left:4px}
.about-lead{font-size:14.5px;line-height:20px;color:var(--ink);margin-bottom:8px}
.about-body{font-size:12.2px;line-height:19px;color:var(--text)}
.btn{display:inline-flex;align-items:center;gap:10px;border:1px solid #bbb;font-size:11.5px;font-weight:600;letter-spacing:.5px;color:var(--ink);text-transform:uppercase;background:var(--white);padding:0 4px 0 14px;height:28px;white-space:nowrap}
.about-text .btn{margin-top:26px}
.inquiry{position:absolute;left:797px;top:53px;width:260px;height:304px;border:1px solid #ddd;background:var(--white)}
.inquiry-head{height:64px;background:var(--navy);clip-path:polygon(0 0,100% 0,100% 68%,50% 100%,0 68%);color:var(--white);text-align:center;font-size:17px;font-weight:500;padding-top:6px}
.inquiry form{padding:16px 14px 0}
.field{height:32px;border:1px solid #d8d8d8;margin-bottom:6px;font-size:11px;color:#555;padding:7px 8px}
.field i{color:#c0282d;font-style:normal}
.field.msg{height:54px}
.inquiry .btn{height:24px;font-size:11px;padding-left:8px;margin-top:2px}

/* mortgages */
.mortgages{position:absolute;top:892px;left:0;width:1200px;height:677px;background:var(--panel)}
.mortgages .title-block{top:50px}
.mortgages .divider{background:#d8d8d8}
.mortgages .divider::after{background:var(--panel)}
.tabs{position:absolute;top:124px;left:141px;width:918px;height:156px;display:flex}
.tab{width:212px;text-align:center;padding-top:22px;font-size:15px;font-weight:500;color:var(--ink);letter-spacing:.4px;margin-right:4px;white-space:nowrap}
.tab svg{display:block;margin:0 auto 16px}
.tab.active{background:var(--white);border:1px solid #d9d9d9;border-bottom:none;border-radius:6px 6px 0 0;height:158px;position:relative;z-index:2}
.tab-panel{position:absolute;top:279px;left:141px;width:918px;height:343px;background:var(--white);border:1px solid #d9d9d9;border-radius:0 8px 8px 8px;padding:20px 28px;font-size:12px;line-height:19px;color:var(--text)}
.tab-panel h4{font-size:15px;font-weight:500;color:var(--navy);margin:12px 0 2px}

/* rent to own */
.rent{position:absolute;top:1569px;left:0;width:1200px;height:472px}
.rent .title-block{top:50px}
.rent .divider{width:380px}
.rent-intro{position:absolute;top:125px;left:141px;width:918px;text-align:center;font-size:14.5px;line-height:20px;color:var(--ink)}
.steps{position:absolute;top:184px;left:236px;display:flex;gap:65px}
.step{width:131px;text-align:center}
.step .ring{width:131px;height:131px;border-radius:50%;border:1px solid #c9c9c9;display:flex;align-items:center;justify-content:center}
.step .disc{width:117px;height:117px;border-radius:50%;background:var(--grey-icon);display:flex;align-items:center;justify-content:center}
.step.active .disc{background:var(--navy)}
.step .label{margin-top:14px;font-size:15.5px;font-weight:500;color:#a8a8a8;letter-spacing:.5px;white-space:nowrap;margin-left:-20px;margin-right:-20px}
.step.active .label{color:var(--navy);font-weight:600}
.step.active .label::after{content:"";display:block;width:100px;height:2px;background:var(--navy);margin:6px auto 0}
.rent-note{position:absolute;top:378px;left:141px;width:918px;text-align:center;font-size:12.5px;line-height:20px;color:var(--text)}

/* testimonials */
.testimonials{position:absolute;top:2041px;left:0;width:1200px;height:350px;background:var(--panel)}
.testimonials .title-block{top:50px}
.testimonials .divider{background:#d8d8d8}
.testimonials .divider::after{background:var(--panel)}
.quotes{position:absolute;top:128px;left:186px;display:flex;gap:38px}
.quote{width:250px;position:relative;padding-left:24px}
.quote::before{content:"";position:absolute;left:0;top:3px;width:16px;height:14px;border-left:5px solid #ccc;border-right:5px solid #ccc}
.quote p{font-size:12.5px;line-height:19px;color:var(--text)}
.quote .who{margin-top:18px;margin-left:-24px;font-size:12.5px;font-weight:600;color:var(--navy)}
.quote .meta{margin-left:-24px;display:flex;justify-content:space-between;font-size:10.5px;color:var(--muted)}
.arrow{position:absolute;top:178px}
.arrow.left{left:140px}
.arrow.right{left:1030px}

/* footer */
.site-footer{position:absolute;top:2391px;left:0;width:1200px;height:224px;background:var(--navy);color:var(--white)}
.f-col h5{font-size:14.5px;font-weight:400;letter-spacing:.8px;text-transform:uppercase;margin-bottom:16px;white-space:nowrap}
.f-col h5 b{font-weight:600}
.f-links{position:absolute;left:141px;top:55px}
.f-links ul{list-style:none;font-size:11.5px;line-height:19px}
.f-links li::before{content:"•";margin-right:8px}
.f-contact{position:absolute;left:327px;top:55px;font-size:11.5px;line-height:17px;white-space:nowrap}
.f-contact .org{font-weight:600;letter-spacing:.4px}
.f-contact .row{display:flex;align-items:center;gap:12px;margin-top:9px}
.f-map{position:absolute;left:585px;top:58px;width:212px;height:131px;background:linear-gradient(135deg,#dfe6d4,#e9e6dc 50%,#d7dde6)}
.f-brand{position:absolute;left:858px;top:100px;font-size:14.5px;font-weight:600;letter-spacing:.4px;white-space:nowrap}
.f-social{position:absolute;left:902px;top:156px;display:flex;gap:26px}
.f-social span{width:22px;height:22px;border-radius:50%;background:#1e88d6;border:2px solid var(--white)}
.copyright{position:absolute;top:2615px;left:0;width:1200px;height:36px;background:var(--footer-bar);color:#eee;font-size:11.5px;text-align:center;line-height:36px}
</style>
</head>
<body>
<div class="topline"></div>
<header class="site-header">
  <div class="brand"><span class="brand-mark"></span>HARBOURLINE LENDING GROUP</div>
  <div class="header-contact hc-address">
    <svg width="20" height="30" viewBox="0 0 20 30"><path d="M10 2a7 7 0 0 0-7 7c0 6 7 13 7 13s7-7 7-13a7 7 0 0 0-7-7z" fill="none" stroke="#25215f" stroke-width="2.2"/><circle cx="10" cy="9" r="2.5" fill="#25215f"/><path d="M1 28h18" stroke="#25215f" stroke-width="2"/></svg>
    <div>4410 Cedar Lane<br>Fairview, Ca 90210</div>
  </div>
  <div class="header-contact hc-phone">
    <svg width="26" height="26" viewBox="0 0 26 26"><path d="M6 3l4 5-2 3c1 3 4 6 7 7l3-2 5 4-3 4C11 23 3 15 3 6z" fill="#25215f"/><path d="M15 4a8 8 0 0 1 7 7M15 8a4 4 0 0 1 3 3" fill="none" stroke="#25215f" stroke-width="1.6"/></svg>
    <div>Call Us On :<br><b>555-014-2290</b></div>
  </div>
</header>

<section class="hero" role="img" aria-label="Photo of a row of new brick and render townhouses under a soft evening sky">
  <nav class="nav">
    <a class="active">Home</a><a class="n-about">About Us</a><a class="n-types">Types of Mortgages</a><a class="n-rent">Rent to Own</a><a class="n-contact">Contact Us</a>
  </nav>
  <div class="nav-social"><span></span><span></span><span></span></div>
  <p class="hero-caption">We Are A <b>Private Lender Of Mortgages</b> And We Provide <b>Rent To Own Housing.</b></p>
  <div class="hero-dots"><i></i><i></i><i class="on"></i></div>
</section>

<section class="about">
  <div class="about-text">
    <h2 class="section-title">ABOUT <b>HARBOURLINE LENDING GROUP</b></h2>
    <div class="divider"></div>
    <p class="about-lead">Harbourline Lending Group is a private lender of 1st,2nd, construction and bridge mortgages in Lakeshore County area.</p>
    <p class="about-body">HLG offers a wide array of financing options to provide assistance to those of you that do not meet the bank’s criteria. The reasons could range from bruised credit to inability to provide the banks with the required documentation to meet income qualification guidelines or simply you need a short term solution and the bank isn’t an option. We are here to help in any way that we can. Please email an outline of your situation and we will analyze it and forward to one of our associated licensed mortgage brokers to contact you and start the process! We Can Put You in Your Own Home Today We know life sometimes delivers challenges and it can be hard to get back on track once you have dealt with challenges.</p>
    <span class="btn">Read More <svg width="22" height="20" viewBox="0 0 22 20"><path d="M2 9l9-7 9 7M5 8v10h12V8" fill="none" stroke="#bbb" stroke-width="1.4"/></svg></span>
  </div>
  <aside class="inquiry">
    <div class="inquiry-head">Quick Inquiry</div>
    <form>
      <div class="field">Name<i>*</i></div>
      <div class="field">Email<i>*</i></div>
      <div class="field">Phone<i>*</i></div>
      <div class="field msg">Message<i>*</i></div>
      <span class="btn">Submit <svg width="20" height="18" viewBox="0 0 22 20"><path d="M2 9l9-7 9 7M5 8v10h12V8" fill="none" stroke="#bbb" stroke-width="1.4"/></svg></span>
    </form>
  </aside>
</section>

<section class="mortgages">
  <div class="title-block">
    <h2 class="section-title">TYPES OF <b>MORTGAGES WE DO</b></h2>
    <div class="divider"></div>
  </div>
  <div class="tabs">
    <div class="tab active">
      <svg width="80" height="66" viewBox="0 0 80 66"><path d="M6 40l17-14 17 14v22H6z" fill="#25215f"/><rect x="19" y="48" width="8" height="14" fill="#fff"/><path d="M42 26l15-12 15 12v16H42z" fill="#25215f"/><path d="M52 8a14 14 0 0 1 16 8" fill="none" stroke="#999" stroke-width="3"/><path d="M30 44a12 12 0 0 0 16 0" fill="none" stroke="#999" stroke-width="3"/></svg>
      Bridge Financing</div>
    <div class="tab">
      <svg width="80" height="66" viewBox="0 0 80 66"><path d="M40 6v50M18 14h44M28 62h24" stroke="#25215f" stroke-width="3"/><path d="M18 14l-10 22h20zM62 14l-10 22h20z" fill="none" stroke="#25215f" stroke-width="2"/><path d="M8 36a10 6 0 0 0 20 0zM52 36a10 6 0 0 0 20 0z" fill="#25215f"/><rect x="44" y="40" width="14" height="16" rx="3" fill="#999"/></svg>
      Debt Consolidation</div>
    <div class="tab">
      <svg width="80" height="66" viewBox="0 0 80 66"><path d="M18 38l16-13 16 13v24H18z" fill="#25215f"/><rect x="30" y="48" width="8" height="14" fill="#fff"/><path d="M30 24a12 12 0 0 1 18-10" fill="none" stroke="#999" stroke-width="4"/><path d="M46 8l6 6-8 3z" fill="#999"/><text x="56" y="28" font-family="Jost,sans-serif" font-size="18" font-weight="700" fill="#999">$</text></svg>
      Equity Take Out</div>
    <div class="tab">
      <svg width="80" height="66" viewBox="0 0 80 66"><path d="M12 36l20-17 20 17v26H12z" fill="#25215f"/><rect x="26" y="46" width="12" height="16" fill="#fff"/><circle cx="56" cy="24" r="14" fill="#fff" stroke="#999" stroke-width="2.5"/><text x="50" y="31" font-family="Jost,sans-serif" font-size="18" font-weight="700" fill="#999">$</text></svg>
      Construction Financing</div>
  </div>
  <div class="tab-panel">
    <p>Are you or your client looking forward to moving into that new property you just purchased, but your possession date is earlier than the sale of your current property? Often, possession dates don’t align in a way that is most convenient, and our bridge financing option will provide the peace of mind while in transition.</p>
    <h4>Problem:</h4>
    <p>Loans are often too short term<br>You don’t want to lose the sales of your property while waiting for financing<br>Existing lenders are not willing or able to bridge the purchase with your existing equity<br>Limited and restrictive conditions cause penalties at traditional financial institutions<br>Your house is listed but hasn’t sold yet</p>
    <h4>Solution:</h4>
    <p>We can help you close the sale of your purchase before the property you are moving out of sells, or before its possession date if it is sold. We offer a short term loan to bridge the gap for you, allowing a less stressful transition between homes. We can also help you take advantage of your prepayment privileges on the house you are selling to help reduce your prepayment penalty.</p>
  </div>
</section>

<section class="rent">
  <div class="title-block">
    <h2 class="section-title">RENT TO <b>OWN A HOME</b></h2>
    <div class="divider"></div>
  </div>
  <p class="rent-intro">We Can Put You in Your Own Home Today We know life sometimes delivers challenges and it can be hard to get back on track once you have dealt with challenges.</p>
  <div class="steps">
    <div class="step active"><div class="ring"><div class="disc">
      <svg width="50" height="56" viewBox="0 0 50 56"><path d="M18 4h14l-4 10h-6z" fill="#fff"/><path d="M20 14h10c12 8 18 20 14 32-2 6-8 8-19 8S8 52 6 46C2 34 8 22 20 14z" fill="#fff"/><text x="18" y="44" font-family="Jost,sans-serif" font-size="20" font-weight="700" fill="#25215f">$</text></svg>
    </div></div><div class="label">Down payment</div></div>
    <div class="step"><div class="ring"><div class="disc">
      <svg width="60" height="56" viewBox="0 0 60 56"><path d="M4 26L30 4l26 22" fill="none" stroke="#fff" stroke-width="4"/><path d="M12 24v28h36V24" fill="none" stroke="#fff" stroke-width="4"/><rect x="20" y="28" width="20" height="14" fill="#fff"/></svg>
    </div></div><div class="label">Household Income</div></div>
    <div class="step"><div class="ring"><div class="disc">
      <svg width="50" height="58" viewBox="0 0 50 58"><path d="M6 2h26l10 10v36H6z" fill="#fff"/><path d="M12 16h18M12 24h22M12 32h14" stroke="#9d9d9d" stroke-width="2.5"/><circle cx="38" cy="44" r="10" fill="#fff" stroke="#9d9d9d" stroke-width="2"/><path d="M33 44l4 4 6-7" fill="none" stroke="#9d9d9d" stroke-width="2.5"/></svg>
    </div></div><div class="label">Credit Report</div></div>
    <div class="step"><div class="ring"><div class="disc">
      <svg width="60" height="58" viewBox="0 0 60 58"><path d="M16 22L32 8l16 14v16H16z" fill="none" stroke="#fff" stroke-width="4"/><path d="M4 40h12l12 6h14c6 0 8-6 14-10v6c-6 8-10 12-16 12H4z" fill="#fff"/></svg>
    </div></div><div class="label">Selecting a House</div></div>
  </div>
  <p class="rent-note">We require a minimum down payment of $10,000 or 3.5% to 4% of total price of the home (whichever is larger).&nbsp;&nbsp;&nbsp; So a $400,000 will require a bigger down than a $300,000 house. This is 100% credited towards your purchase of the home. Your down payment is required at the time we have the home inspection.</p>
</section>

<section class="testimonials">
  <div class="title-block">
    <h2 class="section-title">CLIENT <b>TESTIMONIALS</b></h2>
    <div class="divider"></div>
  </div>
  <svg class="arrow left" width="30" height="50" viewBox="0 0 30 50"><path d="M26 2L4 25l22 23" fill="none" stroke="#c8c8c8" stroke-width="2"/></svg>
  <div class="quotes">
    <div class="quote"><p>Lorem ipsum dolor sit amet, conse ctetuer adipiscing elit, sed diam nonummy nibh euismod tincidunt ut laoreet dolore magna aliquam erat volutpat. Ut wisi enim ad minim veniam, quis nostrud nostrud exerci facilisi.</p><div class="who">- Marissa</div><div class="meta"><span>@ Loren Ipsum</span><span>2 days ago</span></div></div>
    <div class="quote"><p>Lorem ipsum dolor sit amet, conse ctetuer adipiscing elit, sed diam nonummy nibh euismod tincidunt ut laoreet dolore magna aliquam erat volutpat. Ut wisi enim ad minim veniam, quis nostrud nostrud exerci facilisi.</p><div class="who">- Marissa</div><div class="meta"><span>@ Loren Ipsum</span><span>2 days ago</span></div></div>
    <div class="quote"><p>Lorem ipsum dolor sit amet, conse ctetuer adipiscing elit, sed diam nonummy nibh euismod tincidunt ut laoreet dolore magna aliquam erat volutpat. Ut wisi enim ad minim veniam, quis nostrud nostrud exerci facilisi.</p><div class="who">- Marissa</div><div class="meta"><span>@ Loren Ipsum</span><span>2 days ago</span></div></div>
  </div>
  <svg class="arrow right" width="30" height="50" viewBox="0 0 30 50"><path d="M4 2l22 23L4 48" fill="none" stroke="#25215f" stroke-width="2"/></svg>
</section>

<footer class="site-footer">
  <div class="f-col f-links">
    <h5>Quick <b>Links</b></h5>
    <ul><li>Home</li><li>About Us</li><li>Types Of Mortgages</li><li>Rent To Own</li><li>Contact Us</li></ul>
  </div>
  <div class="f-col f-contact">
    <h5>Contact <b>Details</b></h5>
    <div class="org">HARBOURLINE LENDING GROUP</div>
    <div>4410 Cedar Lane, Ca 90210</div>
    <div class="row"><svg width="12" height="12" viewBox="0 0 26 26"><path d="M6 3l4 5-2 3c1 3 4 6 7 7l3-2 5 4-3 4C11 23 3 15 3 6z" fill="#fff"/></svg>123.456.7890</div>
    <div class="row"><svg width="12" height="10" viewBox="0 0 12 10"><rect width="12" height="10" fill="#fff"/><path d="M0 0l6 5 6-5" fill="none" stroke="#25215f" stroke-width="1.2"/></svg>info@harbourlinelending.com</div>
  </div>
  <div class="f-map" role="img" aria-label="Street map showing the office location"></div>
  <div class="f-brand">HARBOURLINE LENDING GROUP</div>
  <div class="f-social"><span></span><span></span><span></span></div>
</footer>
<div class="copyright">Copyright © 2017 HARBOURLINE LENDING GROUP. All Rights Reserved</div>
</body>
</html>
```